Strong, modern, clean Business Card design

Looking for a stunning, but CLEAN business card design. While we are a faith-based organization, we do NOT want this to look religious.

Industry/Entity Type

Non-Profit

Contact Information for Business Card

Dale Munroe | Lead Pastor
dale@BrightHarvestHope.org
970-555-0148
PO Box 7316
Cedar Ridge, NE 80571

Font styles to use
Serif
Sans Serif

Requirements
Should not have
• Religious imagery or symbolism

```html
<!DOCTYPE html>
<html lang="en">
<head>
<meta charset="utf-8">
<title>Dale Munroe – Business Card</title>
<link rel="stylesheet" href="https://fonts.googleapis.com/css2?family=Open+Sans:wght@600;700;800&family=Raleway:wght@700&display=swap">
<style>
  :root {
    --backdrop: #b9dbe0;
    --card: #d8dbd5;
    --navy: #12294a;
    --steel: #4d7a94;
    --mark-text: #e4e6e1;
  }
  * { margin: 0; padding: 0; box-sizing: border-box; }
  html, body {
    width: 1200px; height: 1000px; overflow: hidden;
    background: var(--backdrop);
  }
  .canvas { position: relative; width: 1200px; height: 1000px; }
  .card {
    position: absolute; left: 150px; top: 225px;
    width: 940px; height: 537px;
    background: var(--card);
    border-radius: 22px;
    overflow: hidden;
  }
  .brand-mark {
    position: absolute; left: 84px; top: 83px;
    width: 213px; height: 216px;
    background: var(--steel);
    border-radius: 34px;
    display: flex; align-items: center; justify-content: center;
    text-align: center;
    font-family: "Open Sans", sans-serif;
    font-weight: 700; font-size: 30px; line-height: 1.15;
    color: var(--mark-text);
  }
  .divider {
    position: absolute; left: 387px; top: 85px;
    width: 3px; height: 214px;
    background: var(--steel);
  }
  .identity {
    position: absolute; right: 84px; top: 60px;
    text-align: center;
  }
  .person-name {
    font-family: "Open Sans", sans-serif;
    font-weight: 800; font-size: 56px; letter-spacing: 1.5px;
    color: var(--navy); line-height: 62px;
    white-space: nowrap;
  }
  .person-role {
    font-family: "Raleway", sans-serif;
    font-weight: 700; font-size: 28px; line-height: 34px;
    color: var(--steel); margin-top: 20px;
  }
  .contact-list { list-style: none; }
  .contact-item {
    position: absolute; right: 150px;
    font-family: "Open Sans", sans-serif;
    font-weight: 600; font-size: 26px; line-height: 36px;
    color: var(--navy); text-align: right;
    white-space: nowrap;
  }
  .contact-email { top: 240px; font-size: 25px; }
  .contact-phone { top: 302px; }
  .contact-address { top: 366px; }
  .contact-icon {
    position: absolute; right: -68px; top: 0;
    width: 40px; height: 36px;
  }
  .contact-address .contact-icon { top: -12px; height: 44px; }
  .accent-tab {
    position: absolute; left: 474px; bottom: 0;
    width: 382px; height: 27px;
    background: var(--steel);
    border-radius: 10px 10px 0 0;
  }
</style>
</head>
<body>
<div class="canvas">
  <section class="card">
    <div class="brand-mark">Bright<br>Harvest<br>Hope</div>
    <div class="divider"></div>

    <header class="identity">
      <h1 class="person-name">DALE MUNROE</h1>
      <p class="person-role">Lead Pastor</p>
    </header>

    <ul class="contact-list">
      <li class="contact-item contact-email">dale@brightharvesthope.org
        <svg class="contact-icon" viewBox="0 0 40 36" fill="none" stroke="var(--navy)" stroke-width="2.4" stroke-linejoin="round">
          <rect x="2" y="6" width="36" height="24" rx="2"/>
          <path d="M2 7 L20 21 L38 7"/>
        </svg>
      </li>
      <li class="contact-item contact-phone">+402-555-0148
        <svg class="contact-icon" viewBox="0 0 40 36" fill="none" stroke="var(--navy)" stroke-width="2.4" stroke-linejoin="round">
          <path d="M8 4 L13 3 L17 11 L13 14 Q16 22 23 26 L27 22 L35 26 L34 31 Q31 34 26 33 Q11 28 5 11 Q4 6 8 4 Z"/>
        </svg>
      </li>
      <li class="contact-item contact-address">PO Box 7316<br>Cedar Ridge, NE 80571
        <svg class="contact-icon" viewBox="0 0 40 44" fill="none" stroke="var(--navy)" stroke-width="2.4" stroke-linejoin="round">
          <path d="M20 41 Q7 25 7 16 A13 13 0 0 1 33 16 Q33 25 20 41 Z"/>
          <circle cx="20" cy="16" r="5"/>
        </svg>
      </li>
    </ul>

    <div class="accent-tab"></div>
  </section>
</div>
</body>
</html>
```